Commercial Construction Company

We need a business card design based on our current logo. We are a commercial general contractor based in Southern California that specializes in bank remodels. We would like to see designs that incorporate dark blue. The final design should portray an image of professionalism and quality.

If possible, I would like to add metallic foil to the design. Thank you

```html
<!DOCTYPE html>
<html lang="en">
<head>
<meta charset="utf-8">
<title>Harlow Commercial Building Services – Business Card</title>
<link rel="stylesheet" href="https://fonts.googleapis.com/css2?family=Montserrat:wght@600;700&family=Roboto:wght@400;500&display=swap">
<style>
  :root {
    --stage: #e9e7e4;
    --card-dark: #0b0b0b;
    --card-light: #ffffff;
    --brand-blue: #0d4a84;
    --ink: #111111;
    --text-grey: #555555;
    --band-grey: #a3a3a3;
    --white: #ffffff;
  }
  * { box-sizing: border-box; margin: 0; padding: 0; }
  html, body { width: 1200px; height: 900px; overflow: hidden; }
  body {
    background: var(--stage);
    font-family: "Roboto", Arial, sans-serif;
    display: flex;
    flex-direction: column;
    align-items: center;
    justify-content: center;
    gap: 36px;
  }
  .card {
    width: 700px;
    height: 400px;
    border-radius: 18px;
    position: relative;
    overflow: hidden;
    box-shadow: 0 6px 18px rgba(0,0,0,0.18);
  }

  /* Back side */
  .card--back {
    background: var(--card-dark);
    display: flex;
    flex-direction: column;
    align-items: center;
    justify-content: center;
    gap: 38px;
  }
  .brand {
    display: flex;
    align-items: center;
    gap: 16px;
    font-family: "Montserrat", Arial, sans-serif;
    font-weight: 700;
  }
  .brand__dot {
    width: 22px; height: 22px; border-radius: 50%;
    flex: none;
  }
  .brand__name { line-height: 1.1; text-transform: uppercase; letter-spacing: 0.04em; }
  .card--back .brand__dot { background: var(--white); }
  .card--back .brand__name { color: var(--white); font-size: 26px; text-align: left; }
  .social { display: flex; gap: 10px; }
  .social__badge {
    width: 22px; height: 22px; border-radius: 50%;
    background: var(--brand-blue);
  }

  /* Front side */
  .card--front { background: var(--card-light); }
  .front__logo {
    position: absolute;
    left: 40px; top: 150px;
    width: 270px;
  }
  .card--front .brand__dot { background: var(--ink); }
  .card--front .brand__name { color: var(--ink); font-size: 21px; }
  .front__divider {
    position: absolute;
    left: 345px; top: 80px;
    width: 2px; height: 200px;
    background: var(--brand-blue);
  }
  .contact {
    position: absolute;
    left: 378px; top: 78px;
  }
  .contact__name {
    font-family: "Montserrat", Arial, sans-serif;
    font-weight: 700;
    font-size: 25px;
    color: var(--brand-blue);
    text-transform: uppercase;
    letter-spacing: 0.01em;
    line-height: 1;
  }
  .contact__role {
    font-family: "Montserrat", Arial, sans-serif;
    font-weight: 600;
    font-size: 16px;
    color: var(--ink);
    margin-top: 4px;
  }
  .contact__address {
    font-size: 15px;
    color: var(--text-grey);
    line-height: 1.3;
    margin: 16px 0 8px 36px;
  }
  .contact__list { list-style: none; }
  .contact__item {
    display: flex;
    align-items: center;
    gap: 8px;
    font-size: 15px;
    color: var(--text-grey);
    line-height: 1.45;
  }
  .contact__icon { width: 16px; height: 16px; flex: none; fill: var(--brand-blue); }
  .front__band {
    position: absolute; left: 0; bottom: 0; width: 100%; height: 14px;
    display: flex; align-items: flex-end;
  }
  .front__band-blue { width: 66%; height: 14px; background: var(--brand-blue); }
  .front__band-grey { flex: 1; height: 10px; background: var(--band-grey); }
</style>
</head>
<body>

  <section class="card card--back" aria-label="Card back">
    <div class="brand">
      <span class="brand__dot"></span>
      <span class="brand__name">Harlow Commercial<br>Building Services</span>
    </div>
    <div class="social" aria-label="Social media">
      <span class="social__badge"></span>
      <span class="social__badge"></span>
      <span class="social__badge"></span>
    </div>
  </section>

  <section class="card card--front" aria-label="Card front">
    <div class="front__logo brand">
      <span class="brand__dot"></span>
      <span class="brand__name">Harlow Commercial<br>Building Services</span>
    </div>

    <div class="front__divider"></div>

    <div class="contact">
      <p class="contact__name">Evan Thornbury</p>
      <p class="contact__role">Director</p>
      <p class="contact__address">48 Orchard Bend Road, Suite 110<br>Milford, NJ 07011</p>
      <ul class="contact__list">
        <li class="contact__item">
          <svg class="contact__icon" viewBox="0 0 16 16" aria-hidden="true"><path d="M3.5 1.5l2.5 0 1 3.5-1.6 1.2c.8 1.8 2.1 3.1 3.9 3.9L10.5 8.5l3.5 1v2.5c0 1-1 2-2 2C6.5 14 2 9.5 2 4c0-1 .5-2.5 1.5-2.5z"/></svg>
          555.204.1187
        </li>
        <li class="contact__item">
          <svg class="contact__icon" viewBox="0 0 16 16" aria-hidden="true"><rect x="4" y="1.5" width="8" height="4"/><rect x="1.5" y="5.5" width="13" height="6" rx="1"/><rect x="4" y="9.5" width="8" height="5" fill="#fff" stroke="#0d4a84" stroke-width="1.2"/></svg>
          555.204.1190
        </li>
        <li class="contact__item">
          <svg class="contact__icon" viewBox="0 0 16 16" aria-hidden="true"><rect x="1" y="3.5" width="14" height="9" rx="1"/><path d="M1.5 4l6.5 5 6.5-5" fill="none" stroke="#fff" stroke-width="1.3"/></svg>
          info@yourmail.com
        </li>
        <li class="contact__item">
          <svg class="contact__icon" viewBox="0 0 16 16" aria-hidden="true"><circle cx="8" cy="8" r="7"/><path d="M1.5 8h13M8 1c2.2 2 2.2 12 0 14M8 1c-2.2 2-2.2 12 0 14" fill="none" stroke="#fff" stroke-width="1"/></svg>
          www.yourwebsite.com
        </li>
      </ul>
    </div>

    <div class="front__band">
      <span class="front__band-blue"></span>
      <span class="front__band-grey"></span>
    </div>
  </section>

</body>
</html>
```